Flyer-Design für Lorvex
Zielgruppe
Beratung, Verkauf und Service von Haushaltgeräten im Waschraum und in der Küche
(Dampfabzug, Geschirrspüler, Backofen, Glaskeramik etc. / keine Kleingeräte)
Zielgruppe: Verwaltungen und Eigentümer von Immobilien
Aufgabenstellung
Text: siehe Upload
der Flyer soll ein Blickfang sein und unser junges und temperamentvolles Team unterstreichen.
Vielleicht schwarzer Hintergrund - weisse Schrift - kombiniert mit unserem blau...?

```html
<!DOCTYPE html>
<html lang="de">
<head>
<meta charset="utf-8">
<title>Lorvex Haushaltgeräte AG – Flyer</title>
<link rel="stylesheet" href="https://fonts.googleapis.com/css2?family=Bebas+Neue&family=Open+Sans:wght@400;600;700&family=Raleway:wght@300&display=swap">
<style>
  :root {
    --brand-blue: #31568f;
    --ink: #1e1e1e;
    --body-text: #555a60;
    --white: #ffffff;
    --band-soft: #c8d2e6;
    --photo-dark: #6e6e6e;
    --photo-light: #d9d9d9;
  }
  * { margin: 0; padding: 0; box-sizing: border-box; }
  html, body { width: 848px; height: 1200px; overflow: hidden; background: var(--white); }
  .flyer { position: relative; width: 848px; height: 1200px; background: var(--white); overflow: hidden; }

  .brand {
    position: absolute; left: 196px; top: 62px;
    display: flex; align-items: center; gap: 16px;
  }
  .brand-square { width: 46px; height: 46px; background: var(--brand-blue); }
  .brand-name {
    font-family: "Open Sans", sans-serif; font-weight: 700;
    font-size: 36px; color: var(--ink); letter-spacing: 0.5px;
  }

  .hero-band {
    position: absolute; left: 0; top: 194px; width: 848px; height: 371px;
    background: var(--brand-blue);
  }
  .team-photo {
    position: absolute; left: 55px; top: 240px; width: 278px; height: 278px;
    border-radius: 50%; border: 5px solid var(--white);
    background: radial-gradient(circle at 50% 45%, var(--photo-light), var(--photo-dark));
  }
  .hero-title {
    position: absolute; left: 372px; top: 262px;
    font-family: "Bebas Neue", sans-serif; font-size: 47px; line-height: 44px;
    color: var(--white); letter-spacing: 1px;
  }
  .hero-services {
    position: absolute; left: 372px; top: 385px; list-style: none;
    font-family: "Raleway", sans-serif; font-weight: 300; font-size: 24px;
    line-height: 42px; color: var(--band-soft);
  }

  .section-title {
    position: absolute; left: 64px;
    font-family: "Bebas Neue", sans-serif; font-size: 43px;
    color: var(--brand-blue); letter-spacing: 0.5px;
  }
  .section-list {
    position: absolute; left: 70px; width: 400px;
    font-family: "Open Sans", sans-serif; font-size: 17px; line-height: 28px;
    color: var(--body-text); padding-left: 18px;
  }
  .section-list li::marker { font-size: 13px; }

  .laundry-photo {
    position: absolute; left: 487px; top: 586px; width: 342px; height: 528px;
    background: linear-gradient(160deg, #ececec 0%, #c8ccd2 55%, #9aa2ad 100%);
  }

  .footer-band {
    position: absolute; left: 0; top: 1131px; width: 848px; height: 69px;
    background: var(--brand-blue);
    font-family: "Open Sans", sans-serif; font-size: 15.5px; line-height: 26px;
    color: var(--band-soft); text-align: center; padding-top: 9px;
  }
</style>
</head>
<body>
<main class="flyer">
  <header class="brand">
    <span class="brand-square"></span>
    <span class="brand-name">Lorvex Haushaltgeräte AG</span>
  </header>

  <section class="hero-band"></section>
  <div class="team-photo" role="img" aria-label="Schwarzweiss-Foto des Teams, vier Personen an einer Küchenspüle"></div>
  <h1 class="hero-title">Service und Beratung<br>im Haushalt</h1>
  <ul class="hero-services">
    <li>Haushaltgeräte (EFH und MFH)</li>
    <li>Wäschetrockner/Luftentfeuchter</li>
    <li>professionelle Reinigungsgeräte</li>
  </ul>

  <h2 class="section-title" style="top:622px;">Was wir machen</h2>
  <ul class="section-list" style="top:682px;">
    <li>Installation von Neugeräten</li>
    <li>Reparatur von bestehenden Geräten</li>
    <li>Lösungen zur Optimierung täglicher Hausarbeiten</li>
  </ul>

  <h2 class="section-title" style="top:873px;">Was wir bieten</h2>
  <ul class="section-list" style="top:935px;">
    <li>Beratung direkt vor Ort</li>
    <li>viel Know-How durch laufende Schulungen</li>
    <li>nahezu unbegrenzte Möglichkeiten durch Kooperationen mit Schreinern und Elektrotechnikern</li>
  </ul>

  <div class="laundry-photo" role="img" aria-label="Foto eines Waschsalons mit Reihen von Waschmaschinen, eine Person steckt mit dem Oberkörper in einer Trommel"></div>

  <footer class="footer-band">
    Lorvex Haushaltgeräte AG &nbsp;-&nbsp; Talgartenstrasse 18 &nbsp;-&nbsp; 6030 Ebikon &nbsp;-&nbsp; Tel.: 041 555 37 40<br>
    Fax: 041 555 37 41 &nbsp;-&nbsp; info@lorvex.ch &nbsp;-&nbsp; www.lorvex-haushaltgeraete.ch
  </footer>
</main>
</body>
</html>
```